Baby acupressure app for parents

We need an app for parents that teaches parents how to help them relieve their baby's imbalances (stomach ache, trouble sleeping etc.)

Please see the attached document (with info) and wireframes.

This project is urgent so please only participate if you're able to finish all screens within a few days after the contest is over.

Target Market(s)

Baby moms (20-40 years of age)

Industry/Entity Type

Baby Care

Colors
886aae
b768aa
e667a6
f68d4d
faa54b
fac994
f9ba93
f59195
fee18a

Requirements
Must have
• A high quality design that is both modern and very sleek and stylish.
Nice to have
• Simple animations to make the app "feel" like it's extreme high quality and make the user want to use it again and again
Should not have
• Sandwich menus

```html
<!DOCTYPE html>
<html lang="en">
<head>
<meta charset="utf-8">
<title>Nestly – app screens</title>
<link rel="stylesheet" href="https://fonts.googleapis.com/css2?family=Open+Sans:wght@300;400;600&family=Montserrat:wght@400;500&display=swap">
<style>
  :root{
    --violet:#886aae;
    --orchid:#b768aa;
    --pink:#e667a6;
    --orange:#f68d4d;
    --amber:#faa54b;
    --peach:#fac994;
    --salmon:#f9ba93;
    --rose:#f59195;
    --yellow:#fee18a;
    --stage:#b46aae;
    --ink:#4a4a55;
    --muted:#8a8a95;
    --navbar:#0d0d0f;
    --paper:#ffffff;
  }
  *{box-sizing:border-box;margin:0;padding:0}
  html,body{width:1200px;height:789px;overflow:hidden}
  body{background:var(--stage);font-family:"Open Sans",sans-serif;color:var(--ink);position:relative}

  .screen{position:absolute;width:200px;height:400px;background:var(--paper);display:flex;flex-direction:column;overflow:hidden;box-shadow:0 10px 30px rgba(60,20,70,.28)}
  .screen--featured{width:240px;height:480px}
  .screen--splash{left:20px;top:194px;background:linear-gradient(160deg,var(--violet) 0%,var(--orchid) 55%,var(--pink) 100%)}
  .screen--welcome{left:250px;top:194px}
  .screen--featured{left:480px;top:154px}
  .screen--list{left:750px;top:194px}
  .screen--detail{left:980px;top:194px}

  .status-bar{height:14px;flex:none;display:flex;justify-content:flex-end;align-items:center;gap:4px;padding:0 6px;font-size:6px;color:#fff;background:rgba(0,0,0,.12)}
  .status-bar i{display:block;width:5px;height:5px;background:#fff;border-radius:1px}
  .status-bar--clear{background:transparent}
  .status-bar--light{background:#e9e6ec;color:#777}
  .status-bar--light i{background:#888}

  .nav-bar{height:26px;flex:none;background:var(--navbar);display:flex;justify-content:space-around;align-items:center}
  .nav-bar svg{width:10px;height:10px}

  .body{flex:1;position:relative;display:flex;flex-direction:column;overflow:hidden}

  /* splash */
  .splash{align-items:center;justify-content:center;gap:10px}
  .brand-dot{width:46px;height:46px;border-radius:50%;background:#fff}
  .brand-name{font-size:11px;color:#fff;font-weight:400}

  /* welcome */
  .photo{flex:none;background:linear-gradient(160deg,#e9e4e6,#cdc2c4 60%,#f0d3dc)}
  .welcome .photo{height:150px}
  .welcome-mark{width:44px;height:44px;border-radius:50%;background:var(--violet);align-self:center;margin-top:-24px;border:3px solid #fff}
  .tagline{font-size:8px;color:var(--pink);text-align:center;margin-top:14px}
  .begin{align-self:center;margin-top:10px;width:100px;height:24px;border-radius:12px;background:linear-gradient(90deg,var(--violet),var(--pink));color:#fff;font-size:9px;display:flex;align-items:center;justify-content:center}
  .disclaimer{font-size:4.5px;color:var(--muted);text-align:center;margin:12px 22px 0;line-height:1.4}

  /* play button */
  .play{position:absolute;width:26px;height:26px;border-radius:50%;background:rgba(136,106,174,.9);display:flex;align-items:center;justify-content:center}
  .play svg{width:10px;height:10px}

  /* featured */
  .featured .photo{height:150px;position:relative;background:linear-gradient(150deg,#7c9a4a,#b5b36a 50%,#d9c48e)}
  .featured .play{left:50%;top:50%;transform:translate(-50%,-50%);width:32px;height:32px}
  .featured-title{font-family:"Montserrat",sans-serif;font-weight:400;font-size:14px;color:var(--violet);text-align:center;letter-spacing:1px;margin-top:10px}
  .intro{font-size:5.2px;line-height:1.55;color:var(--muted);text-align:center;margin:6px 14px 0}
  .hint{font-size:5.2px;color:var(--muted);text-align:center;margin-top:6px}

  /* tab bar */
  .tab-bar{flex:none;height:40px;margin-top:auto;background:#fff;display:flex;justify-content:space-around;align-items:flex-end;padding-bottom:4px;border-top:1px solid #eee;position:relative}
  .tab-bar::before{content:"";position:absolute;left:0;right:0;bottom:0;height:14px;background:linear-gradient(90deg,var(--violet),var(--orchid))}
  .tab{position:relative;display:flex;flex-direction:column;align-items:center;gap:2px;font-size:4px;color:#fff;text-transform:uppercase;letter-spacing:.3px}
  .tab-icon{width:20px;height:20px;border-radius:50%;display:flex;align-items:center;justify-content:center;border:2px solid #fff}
  .tab-icon svg{width:10px;height:10px}
  .tab--home .tab-icon{background:var(--violet);width:26px;height:26px}
  .tab--imbalances .tab-icon{background:var(--amber)}
  .tab--about .tab-icon{background:var(--yellow)}

  /* list */
  .list{background:#f4eef4;padding:6px 6px 0;gap:6px}
  .card{flex:1;border-radius:6px;color:#fff;display:flex;flex-direction:column;align-items:center;justify-content:center;gap:5px;box-shadow:0 2px 6px rgba(0,0,0,.1)}
  .card--colic{background:linear-gradient(135deg,#c9a4d6,#a98fc4)}
  .card--growing{background:linear-gradient(135deg,var(--pink),#e99bc4)}
  .card--cough{background:linear-gradient(135deg,#b89ed4,#a27fbf)}
  .card-title{font-size:12px;font-weight:300}
  .card-text{font-size:4.5px;opacity:.9}
  .list .tab-bar{margin:0 -6px 0}

  /* detail */
  .detail .photo{height:120px;position:relative;background:linear-gradient(160deg,#f1ece8,#e7d3c6 60%,#d9c9cf)}
  .detail .play{left:40%;top:52%}
  .back{position:absolute;left:6px;top:4px;width:12px;height:12px}
  .detail-title{font-size:12px;color:var(--violet);text-align:center;margin-top:6px;font-weight:400}
  .detail-text{font-size:4.8px;line-height:1.5;color:var(--muted);text-align:center;margin:5px 14px 0}
  .detail .photo--ear{height:90px;margin:8px 12px 0;border-radius:4px;background:linear-gradient(140deg,#d9a48c,#c57a68 55%,#e15a55)}
</style>
</head>
<body>

<svg width="0" height="0" style="position:absolute">
  <defs>
    <symbol id="nav-back" viewBox="0 0 10 10"><path d="M8 1 L2 5 L8 9 Z" fill="none" stroke="#fff" stroke-width="1"/></symbol>
    <symbol id="nav-home" viewBox="0 0 10 10"><circle cx="5" cy="5" r="3.8" fill="none" stroke="#fff" stroke-width="1"/></symbol>
    <symbol id="nav-recent" viewBox="0 0 10 10"><rect x="1.5" y="1.5" width="7" height="7" fill="none" stroke="#fff" stroke-width="1"/></symbol>
    <symbol id="icon-play" viewBox="0 0 10 10"><path d="M3 1.5 L8.5 5 L3 8.5 Z" fill="#fff"/></symbol>
    <symbol id="icon-calendar" viewBox="0 0 10 10"><rect x="1" y="2" width="8" height="7" rx="1" fill="none" stroke="#fff" stroke-width="1"/><path d="M1 4 H9 M3 1 V3 M7 1 V3" stroke="#fff" stroke-width="1"/></symbol>
    <symbol id="icon-info" viewBox="0 0 10 10"><circle cx="5" cy="2.2" r="0.9" fill="#fff"/><path d="M5 4 V9" stroke="#fff" stroke-width="1.5"/></symbol>
    <symbol id="icon-home" viewBox="0 0 10 10"><circle cx="5" cy="5" r="3" fill="#fff"/></symbol>
  </defs>
</svg>

<!-- splash -->
<section class="screen screen--splash">
  <div class="status-bar status-bar--clear"><i></i><i></i><span>12:30</span></div>
  <div class="body splash">
    <div class="brand-dot"></div>
    <div class="brand-name">Nestly</div>
  </div>
  <nav class="nav-bar"><svg><use href="#nav-back"/></svg><svg><use href="#nav-home"/></svg><svg><use href="#nav-recent"/></svg></nav>
</section>

<!-- welcome -->
<section class="screen screen--welcome">
  <div class="status-bar status-bar--light"><i></i><i></i><span>12:30</span></div>
  <div class="body welcome">
    <div class="photo" role="img" aria-label="Photo of a newborn baby sleeping in a woven nest"></div>
    <div class="welcome-mark"></div>
    <p class="tagline">Help relieve your child's imbalances</p>
    <div class="begin">begin</div>
    <p class="disclaimer">Always consult your doctor if you worry about your child's health and wellbeing.</p>
  </div>
  <nav class="nav-bar"><svg><use href="#nav-back"/></svg><svg><use href="#nav-home"/></svg><svg><use href="#nav-recent"/></svg></nav>
</section>

<!-- featured home -->
<section class="screen screen--featured">
  <div class="status-bar"><i></i><i></i><span>12:30</span></div>
  <div class="body featured">
    <div class="photo" role="img" aria-label="Video still of a parent playing with a toy outdoors">
      <div class="play"><svg><use href="#icon-play"/></svg></div>
    </div>
    <h1 class="featured-title">NESTLY</h1>
    <p class="intro">A short welcome to the app and the gentle pressure points it teaches. Learn simple, calm touch routines that soothe common baby imbalances like colic, poor sleep and tummy ache. Each guide has a short video and clear steps so you can help your little one at home.</p>
    <p class="hint">Tap 'imbalances' to see the full list.</p>
    <div class="tab-bar">
      <div class="tab tab--home"><div class="tab-icon"><svg><use href="#icon-home"/></svg></div>Home</div>
      <div class="tab tab--imbalances"><div class="tab-icon"><svg><use href="#icon-calendar"/></svg></div>Imbalances</div>
      <div class="tab tab--about"><div class="tab-icon"><svg><use href="#icon-info"/></svg></div>About</div>
    </div>
  </div>
  <nav class="nav-bar"><svg><use href="#nav-back"/></svg><svg><use href="#nav-home"/></svg><svg><use href="#nav-recent"/></svg></nav>
</section>

<!-- imbalance list -->
<section class="screen screen--list">
  <div class="status-bar status-bar--light"><i></i><i></i><span>12:30</span></div>
  <div class="body list">
    <div class="card card--colic"><span class="card-title">Colic</span><span class="card-text">Long and frequent crying is hard to deal with.</span></div>
    <div class="card card--growing"><span class="card-title">Growing pains</span><span class="card-text">Aches and pains that come from growth spurts</span></div>
    <div class="card card--cough"><span class="card-title">Coughing etc.</span><span class="card-text">A cough can be hard - help your baby</span></div>
    <div class="tab-bar">
      <div class="tab tab--home"><div class="tab-icon"><svg><use href="#icon-home"/></svg></div>Home</div>
      <div class="tab tab--imbalances"><div class="tab-icon"><svg><use href="#icon-calendar"/></svg></div>Imbalances</div>
      <div class="tab tab--about"><div class="tab-icon"><svg><use href="#icon-info"/></svg></div>About</div>
    </div>
  </div>
  <nav class="nav-bar"><svg><use href="#nav-back"/></svg><svg><use href="#nav-home"/></svg><svg><use href="#nav-recent"/></svg></nav>
</section>

<!-- imbalance detail -->
<section class="screen screen--detail">
  <div class="status-bar status-bar--light"><i></i><i></i><span>12:30</span></div>
  <div class="body detail">
    <div class="photo" role="img" aria-label="Video still of a baby in a bright nursery">
      <svg class="back" viewBox="0 0 12 12"><path d="M10 6 H2 M5 3 L2 6 L5 9" fill="none" stroke="#886aae" stroke-width="1.4"/></svg>
      <div class="play"><svg><use href="#icon-play"/></svg></div>
    </div>
    <h2 class="detail-title">Ear Pain</h2>
    <p class="detail-text">This is some text about the specific imbalance. What could be the reasons for it, is it normal/abnormal, symptoms etc.</p>
    <div class="photo photo--ear" role="img" aria-label="Close-up photo of a child's ear with the sore area highlighted"></div>
    <div class="tab-bar">
      <div class="tab tab--home"><div class="tab-icon"><svg><use href="#icon-home"/></svg></div>Home</div>
      <div class="tab tab--imbalances"><div class="tab-icon"><svg><use href="#icon-calendar"/></svg></div>Imbalances</div>
      <div class="tab tab--about"><div class="tab-icon"><svg><use href="#icon-info"/></svg></div>About</div>
    </div>
  </div>
  <nav class="nav-bar"><svg><use href="#nav-back"/></svg><svg><use href="#nav-home"/></svg><svg><use href="#nav-recent"/></svg></nav>
</section>

</body>
</html>
```